Support People to improve their image and well-being by provided personalised advise

We need a design for business cards that could be used for production on nimbo press. We build a new business in our region for advising mostly women (also men though) on style embracing several aspects including fashion, style, self-confidence and ultimately your internal and external image. The business card should be "classy", "french-style". The business is located in the french -speaking part of Switzerland, close to France. The name of the company is Lumo Trend

Target Market(s)

Service fees won't be cheap (medium to premium) thus we target mid-class to upper-class women (1st target) and men (2nd target)

Industry/Entity Type

Life Coaching

Contact Information for Business Card

Conseil en Image

+41 78 914 63 02
solvedor@lumo-trend.example
linkedin.example/in/dor-vask-solve

Logo Text

Lumo Trend

Colors

Designer to choose colors to be used in the design.

```html
<!DOCTYPE html>
<html lang="fr">
<head>
<meta charset="utf-8">
<title>Lumo Trend – Business Card</title>
<link rel="stylesheet" href="https://fonts.googleapis.com/css2?family=EB+Garamond:wght@400;500&display=swap">
<style>
  :root {
    --page-bg: #f4f4f4;
    --card-black: #0b0b0b;
    --card-charcoal: #1e1e1e;
    --gold: #d4a83a;
    --gold-light: #f1d37a;
    --gold-dark: #8a6416;
    --silver: #d9d9d9;
    --text-light: #e6e6e6;
  }
  * { box-sizing: border-box; margin: 0; padding: 0; }
  html, body {
    width: 1200px;
    height: 900px;
    overflow: hidden;
    background: var(--page-bg);
  }
  .stage {
    width: 1200px;
    height: 900px;
    display: flex;
    align-items: center;
    justify-content: center;
    gap: 50px;
  }
  .card {
    position: relative;
    width: 520px;
    height: 320px;
    border-radius: 24px;
    overflow: hidden;
    background: var(--card-black);
    box-shadow: 0 14px 30px rgba(0,0,0,0.25);
    font-family: "EB Garamond", Georgia, serif;
  }
  .card-texture {
    position: absolute;
    inset: 0;
    background: radial-gradient(ellipse at 45% 50%, var(--card-charcoal) 0%, var(--card-black) 75%);
  }
  .card-back .card-texture {
    background: radial-gradient(ellipse at 55% 40%, #161616 0%, var(--card-black) 70%);
  }

  /* Front */
  .brand-band {
    position: absolute;
    left: 0;
    right: 0;
    top: 136px;
    height: 56px;
    background: rgba(0,0,0,0.75);
    border-top: 2px solid var(--gold);
    border-bottom: 2px solid var(--gold);
  }
  .ornament {
    position: absolute;
    left: 96px;
    width: 178px;
    height: 62px;
    border-radius: 50%;
    background: radial-gradient(ellipse at center, var(--gold-light) 0%, var(--gold) 45%, rgba(138,100,22,0) 75%);
  }
  .ornament-top { top: 68px; }
  .ornament-bottom { top: 198px; }
  .brand-name {
    position: absolute;
    left: 0;
    width: 370px;
    top: 136px;
    height: 56px;
    display: flex;
    align-items: center;
    justify-content: center;
    font-size: 38px;
    font-weight: 400;
    color: var(--silver);
    letter-spacing: 0.5px;
  }

  /* Back */
  .contact {
    position: absolute;
    left: 150px;
    right: 20px;
    top: 100px;
    text-align: center;
    color: var(--text-light);
  }
  .contact-name {
    font-size: 22px;
    font-weight: 500;
    color: var(--gold);
    margin-bottom: 20px;
  }
  .contact-phone {
    font-size: 21px;
    letter-spacing: 0.5px;
    margin-bottom: 4px;
  }
  .contact-line {
    font-size: 15px;
    line-height: 1.35;
  }
</style>
</head>
<body>
  <main class="stage">
    <section class="card card-front">
      <div class="card-texture" role="img" aria-label="Black damask floral pattern background"></div>
      <div class="brand-band"></div>
      <div class="ornament ornament-top" role="img" aria-label="Gold baroque scroll ornament"></div>
      <div class="ornament ornament-bottom" role="img" aria-label="Gold baroque scroll ornament"></div>
      <div class="brand-name">Lumo Trend</div>
    </section>

    <section class="card card-back">
      <div class="card-texture" role="img" aria-label="Faint black damask floral pattern background"></div>
      <div class="contact">
        <p class="contact-name">Dor Vask Solve</p>
        <p class="contact-phone">+41 78 914 63 02</p>
        <p class="contact-line">solvedor@lumo-trend.example</p>
        <p class="contact-line">linkedin.example/in/dor-vask-solve</p>
      </div>
    </section>
  </main>
</body>
</html>
```